Biz Card & Stationary for Business Coaching Co.
Plan. Act. Grow.
Biz Card & Stationary for Business Coaching Co. - Consulting
Creative Brief
Simple
Marlow Quint
CEO
2864 38th Ave S Minneapolis, MN 55406
marlow@brightharbor.net
www.brightharbor.net
My office is home based so we don't need to use the physical address on the card.
I would like to use my logo or at least the logo symbol somehow on the back. Perhaps incorporate tag line "Plan. Act. Grow."

```html
<!DOCTYPE html>
<html lang="en">
<head>
<meta charset="UTF-8">
<title>Bright Harbor Business Cards</title>
<link href="https://fonts.googleapis.com/css2?family=Roboto:wght@300;400;700;900&display=swap" rel="stylesheet">
<style>
  :root {
    --bg: #e4e4e4;
    --paper: #ffffff;
    --blue: #1f5fbf;
    --blue-dark: #173f86;
    --navy: #1b2750;
    --ink: #4a4a4a;
    --grey: #8a8d92;
  }
  * { margin: 0; padding: 0; box-sizing: border-box; }
  html, body { width: 1200px; height: 908px; overflow: hidden; }
  body {
    background: var(--bg);
    font-family: "Roboto", Arial, sans-serif;
    position: relative;
  }
  .card {
    position: absolute;
    width: 560px;
    height: 320px;
    left: 320px;
    background: var(--paper);
    box-shadow: 0 6px 18px rgba(0,0,0,0.12);
    overflow: hidden;
  }
  /* Back */
  .card-back { top: 60px; }
  .back-frame-outer {
    position: absolute; inset: 16px;
    border: 5px solid var(--blue);
  }
  .back-frame-inner {
    position: absolute; inset: 27px;
    border: 2px solid var(--navy);
  }
  .back-mark {
    position: absolute; inset: 0;
    display: flex; flex-direction: column;
    align-items: center; justify-content: center; gap: 14px;
  }
  .mark-row { display: flex; align-items: center; gap: 12px; }
  .mark-dot {
    width: 26px; height: 26px; border-radius: 50%;
    background: var(--blue);
  }
  .mark-name {
    font-weight: 900; font-size: 30px; letter-spacing: 1px;
    color: var(--navy);
  }
  .back-tagline {
    font-size: 15px; font-weight: 400; letter-spacing: 3px;
    color: var(--blue);
    text-transform: uppercase;
  }
  /* Front */
  .card-front { top: 500px; }
  .front-brand {
    position: absolute; left: 30px; top: 34px;
  }
  .front-brand .mark-dot { width: 22px; height: 22px; }
  .front-brand .mark-row { gap: 10px; }
  .front-brand .mark-name { font-size: 26px; }
  .brand-tagline {
    margin-top: 4px; margin-left: 32px;
    font-size: 9px; letter-spacing: 1.5px; color: var(--grey);
    text-transform: uppercase;
  }
  .name-band {
    position: absolute; right: 0; top: 34px;
    width: 250px; height: 64px;
    background: var(--blue);
    color: #fff;
    padding: 10px 18px;
  }
  .person-name { font-size: 20px; font-weight: 400; letter-spacing: 1px; text-transform: uppercase; }
  .person-role { font-size: 15px; font-weight: 300; margin-top: 2px; }
  .phones {
    position: absolute; right: 40px; top: 112px;
    width: 192px;
    font-size: 12px; color: var(--ink); line-height: 1.45;
  }
  .contact {
    position: absolute; right: 40px; top: 160px;
    width: 192px;
    font-size: 12px; color: var(--ink); line-height: 1.5;
  }
  .front-band { position: absolute; left: 0; bottom: 0; width: 560px; height: 92px; }
</style>
</head>
<body>

  <section class="card card-back" aria-label="Card back">
    <div class="back-frame-outer"></div>
    <div class="back-frame-inner"></div>
    <div class="back-mark">
      <div class="mark-row">
        <span class="mark-dot"></span>
        <span class="mark-name">BRIGHT HARBOR</span>
      </div>
      <p class="back-tagline">Plan. Act. Grow.</p>
    </div>
  </section>

  <section class="card card-front" aria-label="Card front">
    <div class="front-brand">
      <div class="mark-row">
        <span class="mark-dot"></span>
        <span class="mark-name">BRIGHT HARBOR</span>
      </div>
      <p class="brand-tagline">Business Coaching &amp; Consulting</p>
    </div>

    <div class="name-band">
      <p class="person-name">Marlow Quint</p>
      <p class="person-role">CEO</p>
    </div>

    <div class="phones">
      <p>012 555 0148</p>
      <p>012 555 0149</p>
    </div>

    <div class="contact">
      <p>marlow@brightharbor.net</p>
      <p>www.brightharbor.net</p>
    </div>

    <svg class="front-band" viewBox="0 0 560 92" aria-hidden="true">
      <path d="M0 38 C160 20 360 30 560 44 L560 92 L0 92 Z" fill="#8a8d92"/>
      <path d="M0 48 C160 32 360 42 560 56 L560 92 L0 92 Z" fill="#1f5fbf"/>
      <path d="M0 72 C200 60 380 66 560 78 L560 92 L0 92 Z" fill="#173f86"/>
      <g fill="#ffffff" stroke="#8a8d92" stroke-width="2">
        <circle cx="40" cy="42" r="9"/>
        <circle cx="300" cy="37" r="9"/>
      </g>
      <path d="M36 38 q0 6 8 8 l2 -2 l-2 -2 l-1 1 q-3 -1 -4 -4 l1 -1 l-2 -2 z" fill="#1f5fbf"/>
      <g fill="none" stroke="#1f5fbf" stroke-width="1.5">
        <rect x="295" y="33.5" width="10" height="7"/>
        <path d="M295 33.5 l5 4 l5 -4"/>
      </g>
    </svg>
  </section>

</body>
</html>
```